High End Cosmetic Packaging Design Project

Looking for packaging for 2 products for a High end skin care line aimed at the 35+ year old women. Color scheme is Pantone 2765c with accents of metallic silver, copper or gold, Pantone colors 871-877c. Possible watermark in the background or a 3D image. We are open to any good ideas and suggestions. Box dimensions for the 2 products are small, approximately 4.375 inches high and 1.5 inches square. I have attached an image of the logo. I have the logo files in all the various forms. 1 box is for a Vitamin C Serum and the other box is for an Anti Aging Serum. Boxes are the same but the text will be different on both products. I will supply the text for the boxes later, including directions & ingredients and a UPC code that has to go on the underside of the box. It has to be an elegant design that will stand out in photos online. Good and quick communication & feedback between you and us is essential. I have attached a jpg of our new logo. I have this logo in all available forms
*****We are open to all ideas and want your ideas and input. The bottles that go inside these boxes are a deep violet almost black velkar glass. This is where the pantone color selection came from but upon further thought it may not be the right choice. We were out looking at cosmetic packaging today and thought also as an idea that a dark charcoal, or black box might work as well. We have seen boxes in those dark shades in glossy, matt and some with a sparkle finish. Embossed lettering may be a possibility as well. Copper letters may be an idea that works well also. These are just ideas rolling aroung in our heads but please give us your ideas*******
This is for the 35+ year old woman.
Communication

```html
<!DOCTYPE html>
<html lang="en">
<head>
<meta charset="utf-8">
<title>Serum Carton Dielines</title>
<link rel="stylesheet" href="https://fonts.googleapis.com/css2?family=Raleway:wght@300;400&display=swap">
<style>
  :root {
    --page: #ffffff;
    --die-silver: #bfc0c2;
    --die-gold: #b9dedd;
    --silver-dark: #a9abae;
    --silver-light: #e8e9ea;
    --gold-dark: #94825a;
    --gold-light: #d6ccb2;
    --label-text: #ffffff;
    --brand-silver: #a7a9ac;
    --brand-gold: #9a8760;
  }
  html, body {
    margin: 0;
    width: 1200px;
    height: 807px;
    overflow: hidden;
    background: var(--page);
  }
  .artboard { display: block; width: 1200px; height: 807px; }
  .dieline { fill: none; stroke-width: 1; }
  .dieline--silver { stroke: var(--die-silver); }
  .dieline--gold { stroke: var(--die-gold); }
  .label-text {
    font-family: "Raleway", sans-serif;
    font-weight: 300;
    fill: var(--label-text);
    text-anchor: middle;
  }
  .brand-name {
    font-family: "Raleway", sans-serif;
    font-weight: 300;
    font-size: 24px;
    letter-spacing: 3px;
    text-anchor: middle;
  }
  .brand-name--silver { fill: var(--brand-silver); }
  .brand-name--gold { fill: var(--brand-gold); }
</style>
</head>
<body>
<svg class="artboard" viewBox="0 0 1100 740" preserveAspectRatio="none" xmlns="http://www.w3.org/2000/svg">
  <defs>
    <linearGradient id="silver-label" x1="0" y1="0" x2="1" y2="1">
      <stop offset="0" stop-color="var(--silver-dark)"/>
      <stop offset="1" stop-color="var(--silver-light)"/>
    </linearGradient>
    <linearGradient id="silver-band" x1="0" y1="0" x2="0" y2="1">
      <stop offset="0" stop-color="#c3c4c6"/>
      <stop offset="1" stop-color="#ecedee"/>
    </linearGradient>
    <linearGradient id="gold-label" x1="1" y1="1" x2="0" y2="0">
      <stop offset="0" stop-color="var(--gold-dark)"/>
      <stop offset="1" stop-color="var(--gold-light)"/>
    </linearGradient>
    <linearGradient id="gold-band" x1="0" y1="0" x2="0" y2="1">
      <stop offset="0" stop-color="#cbc0a3"/>
      <stop offset="1" stop-color="#ebe6da"/>
    </linearGradient>

    <g id="carton-dieline">
      <!-- glue flap -->
      <path d="M86 215 L48 218 V538 L86 541"/>
      <!-- body panels -->
      <rect x="86" y="215" width="460" height="326"/>
      <path d="M202 215 V541 M316 215 V541 M432 215 V541"/>
      <!-- top tuck flap -->
      <path d="M316 215 V100 H322 V107 H426 V100 H432 V215"/>
      <path d="M322 100 C322 72 345 53 374 53 C403 53 426 72 426 100"/>
      <!-- top dust flaps -->
      <path d="M202 215 V190 L215 185 L220 162 H316"/>
      <path d="M432 162 H528 L533 185 L546 190 V215"/>
      <!-- bottom tuck flap -->
      <path d="M86 541 V655 H92 V648 H196 V655 H202 V541"/>
      <path d="M92 655 C92 684 115 709 144 709 C173 709 196 684 196 655"/>
      <!-- bottom dust flaps -->
      <path d="M202 541 V595 H296 L302 570 L316 563"/>
      <path d="M316 541 V552 L322 555 V570 H426 V555 L432 552 V541"/>
      <path d="M432 548 L446 555 L451 580 H546 V541"/>
    </g>
  </defs>

  <!-- Vitamin C carton -->
  <g class="carton carton--vitamin-c">
    <rect class="side-band" x="86" y="215" width="116" height="326" fill="url(#silver-band)"/>
    <use href="#carton-dieline" class="dieline dieline--silver"/>

    <g class="product-label" transform="rotate(180 373 158)">
      <rect x="330" y="116" width="86" height="85" fill="url(#silver-label)"/>
      <text class="label-text" x="373" y="152" font-size="19">VITAMIN</text>
      <text class="label-text" x="373" y="175" font-size="19">C</text>
    </g>
    <g class="product-label">
      <rect x="216" y="232" width="86" height="86" fill="url(#silver-label)"/>
      <text class="label-text" x="259" y="270" font-size="19">VITAMIN</text>
      <text class="label-text" x="259" y="294" font-size="19">C</text>
    </g>
    <g class="product-label">
      <rect x="445" y="232" width="88" height="86" fill="url(#silver-label)"/>
      <text class="label-text" x="489" y="270" font-size="19">VITAMIN</text>
      <text class="label-text" x="489" y="294" font-size="19">C</text>
    </g>
    <g class="product-label">
      <rect x="332" y="416" width="87" height="86" fill="url(#silver-label)"/>
      <text class="label-text" x="375" y="454" font-size="19">VITAMIN</text>
      <text class="label-text" x="375" y="478" font-size="19">C</text>
    </g>

    <text class="brand-name brand-name--silver" transform="translate(374 318) rotate(90)" y="8">LUMERA LABS</text>
  </g>

  <!-- Anti Aging Serum carton -->
  <g class="carton carton--anti-aging" transform="translate(518 6)">
    <rect class="side-band" x="86" y="215" width="116" height="326" fill="url(#gold-band)"/>
    <use href="#carton-dieline" class="dieline dieline--gold"/>

    <g class="product-label" transform="rotate(180 374 159)">
      <rect x="330" y="117" width="89" height="85" fill="url(#gold-label)"/>
      <text class="label-text" x="374" y="150" font-size="12">ANTI AGING</text>
      <text class="label-text" x="374" y="174" font-size="20">SERUM</text>
    </g>
    <g class="product-label">
      <rect x="216" y="232" width="89" height="87" fill="url(#gold-label)"/>
      <text class="label-text" x="260" y="266" font-size="12">ANTI AGING</text>
      <text class="label-text" x="260" y="292" font-size="20">SERUM</text>
    </g>
    <g class="product-label">
      <rect x="445" y="232" width="89" height="87" fill="url(#gold-label)"/>
      <text class="label-text" x="489" y="266" font-size="12">ANTI AGING</text>
      <text class="label-text" x="489" y="292" font-size="20">SERUM</text>
    </g>
    <g class="product-label">
      <rect x="330" y="417" width="89" height="86" fill="url(#gold-label)"/>
      <text class="label-text" x="374" y="451" font-size="12">ANTI AGING</text>
      <text class="label-text" x="374" y="477" font-size="20">SERUM</text>
    </g>

    <text class="brand-name brand-name--gold" transform="translate(374 318) rotate(90)" y="8">LUMERA LABS</text>
  </g>
</svg>
</body>
</html>
```